Book cover entitled #GLOWBEYONDIT

Design front book cover (self-self-portait photos included) for my first book entitled -

#GLOWBEYONDIT (may be best to have different shades of colour for glow beyond it to stand off you). I'm intentionally choosing a title that is essentially a hashtag.

Subtitle - Rewriting quiet inner battles

Concept of cover - left side of my face is shaded with shame and right side is brighter and hopeful. I have also include my logo.

Link for photos
https://www.filqorvex.com/sh/tq7mxd2kw9pl41a/BBR8NpXwQ3hLm6TzvKe2YUJ5b?dl=0

Target Market(s)

People (or friends & family) suffering with the shame of mental health struggles

Industry/Entity Type

Mental Health

Font styles to use
Other font styles liked:
• Avenir

Colors
3276b5
85acd3
cfdeed

Requirements
Must have
• Relatable, contemporary, authentic & compelling
• Link for photos
• https://www.filqorvex.com/sh/tq7mxd2kw9pl41a/BBR8NpXwQ3hLm6TzvKe2YUJ5b?dl=0
Nice to have
• Abstract & creative
Should not have
• Cheesy, plastic, pedestrian etc

```html
<!DOCTYPE html>
<html lang="en">
<head>
<meta charset="utf-8">
<title>#GlowBeyondIt – Book Cover</title>
<link href="https://fonts.googleapis.com/css2?family=Josefin+Sans:wght@400&family=Nunito+Sans:wght@600;700&display=swap" rel="stylesheet">
<style>
  :root {
    --stage: #e9e8e6;
    --cover-black: #050505;
    --skin-light: #8a6b55;
    --skin-mid: #5c4535;
    --skin-shadow: #2e231c;
    --hair-grey: #3a3a3c;
    --shirt-dark: #141516;
    --title-white: #ffffff;
    --author-white: #eef1f4;
    --subtitle-blue: #1f8fd8;
  }
  * { margin: 0; padding: 0; box-sizing: border-box; }
  html, body {
    width: 1200px;
    height: 800px;
    overflow: hidden;
    background: var(--stage);
  }
  .canvas {
    position: relative;
    width: 1200px;
    height: 800px;
  }
  .book-cover {
    position: absolute;
    left: 360px;
    top: 18px;
    width: 480px;
    height: 764px;
    background: var(--cover-black);
    overflow: hidden;
  }
  .portrait {
    position: absolute;
    inset: 0;
    background:
      radial-gradient(ellipse 17% 11% at 53% 21%, var(--hair-grey) 0%, #202022 60%, transparent 100%),
      radial-gradient(ellipse 18% 20% at 55% 40%, var(--skin-light) 0%, var(--skin-mid) 45%, var(--skin-shadow) 75%, transparent 100%),
      radial-gradient(ellipse 60% 30% at 55% 80%, #2a2b2d 0%, var(--shirt-dark) 55%, transparent 100%),
      linear-gradient(90deg, #030303 0%, #0d0c0b 55%, #060606 100%);
  }
  .author-name {
    position: absolute;
    top: 42px;
    left: 0;
    right: 0;
    text-align: center;
    font-family: "Josefin Sans", sans-serif;
    font-weight: 400;
    font-size: 35px;
    letter-spacing: 5px;
    color: var(--author-white);
  }
  .title-block {
    position: absolute;
    left: 62px;
    right: 22px;
    bottom: 34px;
  }
  .book-title {
    font-family: "Nunito Sans", sans-serif;
    font-weight: 700;
    color: var(--title-white);
    line-height: 0.92;
    letter-spacing: -1px;
    white-space: nowrap;
  }
  .book-title .line-one { display: block; font-size: 106px; }
  .book-title .line-two { display: block; font-size: 76px; margin-top: 8px; }
  .book-subtitle {
    margin-top: 14px;
    font-family: "Nunito Sans", sans-serif;
    font-weight: 600;
    font-size: 19px;
    letter-spacing: 2px;
    color: var(--subtitle-blue);
    text-transform: uppercase;
    white-space: nowrap;
  }
</style>
</head>
<body>
<main class="canvas">
  <section class="book-cover">
    <div class="portrait" role="img" aria-label="Moody low-key head-and-shoulders portrait photograph of the author in a dark shirt against a black background"></div>
    <p class="author-name">DEAN HOLLOWAY</p>
    <div class="title-block">
      <h1 class="book-title">
        <span class="line-one">#GLOW</span>
        <span class="line-two">BEYOND IT</span>
      </h1>
      <p class="book-subtitle">Rewriting quiet inner battles</p>
    </div>
  </section>
</main>
</body>
</html>
```